BENEATH THE [HARBOR] OF A DAWN, Mend your road

We are looking for a cover refresh of an existing bestselling book that is going into 3rd edition print this year.
The book is an inspirational as well as educational book that has become recognized as one of the most comprehensive, actionable, personal and financial planning resources available today for families, individuals and business owners alike.
Comprised of three true stories of loss, learning to live and love again and a 30 page checklist at the back of the book it contains tips and strategies for everyone to help them to get their personal and financial lives in order while they can.
The cover must have the following:
1. Appeal to a broad audience/both personal and corporate
2. Include Mara Quellton Bestselling Author
3. Include introduction of a new Afterword
4. 3rd Edition
5. Colors to remain the same – red, black and white
6. The title must remain in caps and the word [HARBOR] must have the brackets around it
We have also added a current copy of the second edition to help you. For your information our website is www.thequelltonhouse.example
Reason: We have narrowed it down to our top 3 designs. We are submitting the covers to our community for them to pick the top cover. Good luck to everyone

```html
<!DOCTYPE html>
<html lang="en">
<head>
<meta charset="utf-8">
<title>Beneath the [Harbor] of a Dawn — 3rd Edition Cover</title>
<link href="https://fonts.googleapis.com/css2?family=Open+Sans:wght@400;600&family=Arimo:wght@400&display=swap" rel="stylesheet">
<style>
  :root {
    --paper: #ffffff;
    --ink: #111111;
    --spine-red: #bd2c2c;
    --frame: #1a1a1a;
    --portrait-light: #fbfbfb;
    --portrait-warm: #b8764a;
    --portrait-dark: #2a2a2a;
  }
  html, body {
    margin: 0;
    padding: 0;
    width: 1200px;
    height: 1200px;
    overflow: hidden;
    background: var(--paper);
  }
  .canvas {
    position: relative;
    width: 1200px;
    height: 1200px;
    background: var(--paper);
  }
  .cover {
    position: absolute;
    left: 205px;
    top: 8px;
    width: 780px;
    height: 1160px;
    border: 2px solid var(--frame);
    background: var(--paper);
    box-sizing: border-box;
    overflow: hidden;
  }
  .spine-band {
    position: absolute;
    left: 0;
    top: 0;
    width: 47px;
    height: 100%;
    background: var(--spine-red);
  }
  .edition {
    position: absolute;
    right: 42px;
    top: 152px;
    font-family: "Open Sans", sans-serif;
    font-weight: 600;
    font-size: 29px;
    color: var(--ink);
    margin: 0;
  }
  .edition sup {
    font-size: 16px;
    vertical-align: 12px;
  }
  .title {
    position: absolute;
    left: 66px;
    right: 40px;
    top: 196px;
    margin: 0;
    display: flex;
    justify-content: space-between;
    align-items: center;
    font-family: "Open Sans", sans-serif;
    font-weight: 400;
    color: var(--ink);
  }
  .title-lead {
    display: flex;
    flex-direction: column;
    font-size: 38px;
    line-height: 50px;
    letter-spacing: -1px;
    white-space: nowrap;
  }
  .title-key {
    font-size: 84px;
    line-height: 1;
    letter-spacing: 1px;
    white-space: nowrap;
  }
  .portrait {
    position: absolute;
    left: 57px;
    top: 380px;
    width: 704px;
    height: 620px;
    background:
      radial-gradient(ellipse 30% 34% at 52% 40%, var(--portrait-warm) 0%, rgba(184,118,74,0.55) 55%, rgba(251,251,251,0) 100%),
      linear-gradient(180deg, var(--portrait-light) 0%, var(--portrait-light) 70%, #d9d9d9 85%, var(--portrait-dark) 100%);
  }
  .author-line {
    position: absolute;
    left: 66px;
    right: 40px;
    bottom: 26px;
    margin: 0;
    text-align: right;
    font-family: "Arimo", sans-serif;
    font-weight: 400;
    font-size: 46px;
    line-height: 1;
    color: var(--ink);
    white-space: nowrap;
  }
</style>
</head>
<body>
  <div class="canvas">
    <div class="cover">
      <div class="spine-band"></div>
      <p class="edition">3<sup>rd</sup> Edition</p>
      <h1 class="title">
        <span class="title-lead">
          <span>BENEATH THE</span>
          <span>OF A DAWN</span>
        </span>
        <span class="title-key">[HARBOR]</span>
      </h1>
      <div class="portrait" role="img" aria-label="Portrait photograph of the author, smiling, in a black and white jacket against a white backdrop"></div>
      <p class="author-line">Mara Quellton Bestselling Author</p>
    </div>
  </div>
</body>
</html>
```